Velmora Gems - High end custom Jewelry website

I need a web design for an online custom jewelry company called Velmora Gems. (www.velmoragems-example.com) this company specializes in high-end custom made engagement rings, wedding bands and jewelry of all kinds (necklaces, earrings, bracelets etc)All our jewelry uses diamonds so there must be a focus on diamonds on every type of jewelry we will be designing off the website.

We are a company located in New York City but our website will
aim to cater to international, national clients and as well as New York city residents.The company low overhead provides diamonds and precious metal at a discounted costs compared to its competitors. Velmora Gems makes unique custom diamond jewelry of a higher quality and at a lower price than carriage trade retail jewellers. (meaning that our company allows our customers to save money on diamond jewelry then they would if they bought from any known store or company)

The website will act as a tool for our customers to create their own jewelry. The way they will do this is by uploading pictures of what they like, they can post any pictures they want (from drawings, to actual copy and pasted pictures from other websites of designs) From these designs we will create a 3D digital image of the jewelry they like and customize it - however they want (colours, size etc) and then give them a quote in price. From the quote they will either approve it and we can have it made for them in 1 weeks time. If they decline it we will try to do whatever it is they want for the design to suit their needs.

We want the website to be simple and user friendly since people will be working on it to create their own individual jewelry pieces. Therefore some useful headings should include:

"Custom Jewellery" or something like "your design" "Custom Design"

a drop heading here should show the following steps into creating the jewelry.

step 1:
upload pictures of the designs you like
step 2:
What is your ring size?
Step 3:
What setting would you like your ring in? platinum, 14k etc..
Step 4:
What is your budget?
Step 5 :
Once you’ve uploaded pictures and give an explanation of what you want then we will contact you by phone or email and proceed to design your ring. Give us your contact info in this step.

Other then that other headings id like to see on the site are:

"Home"
main page with appealing picture which I can later add text to it explaining our company

"About us"
will include a brief section of who we are

"Wedding/engagment"

We are based in New York City and our company offers a one-to-one personal service to our clients ensuring their expectations are well met and, if we can help it, surpassed. We are a personal shopping and diamond supplier to individuals. Custom design is our speciality weather it be wedding ring, engagement ring or anniversary ring we aim to create distinctive designs that both reflect your personality as well as the beauty of the gemstones used in your piece. We use platinum, 14l-18k gold and diamonds to whatever it is that you may desire.
We in our company believe that we are privileged to be a part of one of the biggest events in our customer’s lives, and we pride ourselves on making sure that our customers have the best experience possible. As the diamond is the center piece of every engagement ring, we at VG make sure that our clients find the best diamond possible that is within their budget. Similarly, we work with established jewellery artisans from Belgium to provide the highest possible craftsmanship to a ring design of your choice. We make sure that our rings are made by the true and tried traditional methods focused on quality rather than quantity and of course our diamonds are QRB certified.

Diamonds

A section that explains where our diamonds come from. A heading will drop down here that is a diamond guide, as shown below.
Diamond Guide

An overview of the 4 C’s and different settings, a section for a brief education on diamonds.
Client Experiences

A section where clients share their experiences with Velmora Gems and can post pictures and share stories about their engagement etc.

The colour i would like to see are white and black, white and dark blue or royal blue. I don't think pastel colours will look good with this, maybe accents of purple or something pastel but for the main colours I want to keep it classic and sophisticated since it is a diamond company.

"Sign in | Check out"
where users are able to create a profile and upload their pictures and create their designs..

and a "search section"

or something along these lines or if you can incorporate both:

Exquisite craftsmanship Finest quality diamonds
Will beat any competitors price by twenty to seventy percent guaranteed
Price quotes whitin24 hours

Upload design picture or sketch
Receive price quote within 24hours
Receive and approve free customized design
Receive you jewelry in 1 week or less

Engagment Ring or necklace, earring, etc
Name
EMail
phone
Competitior Link
Budget

The final design should communicate that Velmora Gems is a custom jewelry site that allows individuals to personalize any type of jewellery they want with diamonds - at a fraction of the cost in comparison to any other out there. Our team works very hard to ensure that you will be so involved in the custom order process that there is no chance of something not being made to your requests. Jewelry is made to the highest standard or it does not ship in the first place. In the event a custom order does not suit a customer, we will take returns within 14 days of delivery less a 25% restocking fee.

Target Market(s)

middle class and upper class people ages 25-45

Industry/Entity Type

Digital

Requirements
Must have
• We have the logo now that I will attach BUT if you want to design something else please feel free ! I am open to all designs and ideas.
My logo now is simply a sketch so even if we make it look a bit more professional and classy I would like that, I think I want to keep it simple just black and white and maybe make the diamond shiny if possible. other then black in white I liked the gold and black combination too.. but as I said open to any other creative ideas!

can take pictures of jewelry off this website:
http://www.plindrowatelier-example.com/library/rings.html
Nice to have
• We already have a logo but we would like to see a banner or something that indicated saving money on diamond jewelry without it looking tacky or too cheap..

Also would like to see artistic pictures if you can of jewelry alongside very simple designs of jewelry that the masses like, (anything trendy or appealing to the eye)

cursive or elegant writing could be nice, flash could also be incorporated in the main page..

Should not have
• Nothing to old fashioned, when I mean elegant maybe just the the name of the company in cursive writing (Velmora Gems) but the actual headings and font on the website to be in a widely used font on jewelry websites. Please no hot pink colours or anything neon..
no times new roman font..

```html
<!DOCTYPE html>
<html lang="en">
<head>
<meta charset="utf-8">
<title>Velmora Gems — Custom Diamond Jewellery</title>
<link href="https://fonts.googleapis.com/css2?family=PT+Sans:wght@400;700&family=PT+Sans+Narrow:wght@400;700&display=swap" rel="stylesheet">
<style>
  :root {
    --page-bg: #141416;
    --footer-bg: #2b2b2d;
    --footer-rule: #6a6a6c;
    --text: #ffffff;
    --muted: #c9c9cb;
    --tagline: #b9b9bb;
    --navy: #163a7a;
    --ink: #2a2a2c;
    --nav-top: #3d3d40;
    --nav-bottom: #1d1d1f;
    --nav-border: #6b6b6e;
    --frame: #2e2e30;
    --field-border: #6a6a6c;
  }
  * { box-sizing: border-box; margin: 0; padding: 0; }
  html, body { width: 1016px; height: 1200px; overflow: hidden; }
  body {
    position: relative;
    background: var(--page-bg);
    color: var(--text);
    font-family: "PT Sans", Arial, sans-serif;
  }
  .abs { position: absolute; }
  a { color: inherit; text-decoration: none; }

  /* Header */
  .brand {
    left: 121px; top: 10px; width: 139px; height: 114px;
    background: #0c0c0d;
    display: flex; flex-direction: column; align-items: center; justify-content: center; gap: 10px;
  }
  .brand-mark { width: 22px; height: 22px; border: 2px solid var(--text); }
  .brand-name { font-size: 17px; font-weight: 700; color: var(--text); letter-spacing: .5px; }

  .account-links {
    right: 116px; top: 27px;
    font-size: 12px; color: var(--text);
  }
  .account-links span.sep { margin: 0 7px; }
  .account-links .cart { font-weight: 700; }

  .search {
    left: 702px; top: 69px; width: 200px; height: 30px;
    background: #f4f4f4; border-radius: 5px;
    display: flex; align-items: center; justify-content: space-between;
    padding: 0 10px 0 12px;
    font-size: 10px; color: #333;
  }

  .main-nav {
    left: 121px; top: 135px; width: 780px; height: 44px;
    border: 1px solid var(--nav-border); border-radius: 4px;
    background: linear-gradient(var(--nav-top), var(--nav-bottom));
    display: flex; align-items: center; padding-left: 12px;
  }
  .main-nav a {
    font-family: "PT Sans Narrow", "Arial Narrow", sans-serif;
    font-size: 12.5px; font-weight: 400; letter-spacing: .2px;
    padding: 0 15px; line-height: 28px;
    border-right: 1px solid #5a5a5d;
  }
  .main-nav a:last-child { border-right: none; }

  /* Hero */
  .hero { left: 124px; top: 194px; width: 774px; height: 290px; background: var(--frame); }
  .hero-panel { position: absolute; left: 7px; top: 7px; right: 8px; bottom: 7px; background: #ffffff; }
  .hero-photo {
    position: absolute; left: 10px; top: 8px; width: 330px; height: 268px;
    background: radial-gradient(ellipse at 45% 45%, #f3f4f6 0%, #c9ccd1 55%, #ffffff 85%);
  }
  .hero-title {
    position: absolute; left: 399px; top: 50px;
    font-family: "PT Sans Narrow", sans-serif; font-weight: 700;
    font-size: 33px; color: var(--navy); letter-spacing: .3px;
  }
  .hero-sub {
    position: absolute; left: 399px; top: 106px;
    font-family: "PT Sans Narrow", sans-serif; font-weight: 700;
    font-size: 20px; color: #2f2f31;
  }
  .hero-button {
    position: absolute; left: 399px; top: 166px; width: 168px; height: 38px;
    background: linear-gradient(#5a5a5c, #1f1f21); border-radius: 3px;
    display: flex; align-items: center; justify-content: center;
    font-family: "PT Sans Narrow", sans-serif; font-weight: 700; font-size: 15px; color: #fff;
  }
  .hero-note {
    position: absolute; left: 399px; top: 215px;
    font-size: 12px; font-weight: 700; color: #222;
  }
  .hero-dots { position: absolute; left: 342px; top: 257px; display: flex; gap: 4px; }
  .hero-dots span { width: 12px; height: 12px; border-radius: 50%; background: #000; }
  .hero-dots span.active { background: #888; }

  /* Welcome */
  .welcome-title {
    left: 0; width: 1016px; top: 499px; text-align: center;
    font-family: "PT Sans Narrow", sans-serif; font-weight: 700; font-size: 12px;
  }
  .welcome-text {
    left: 122px; top: 527px; width: 778px; text-align: center;
    font-size: 10px; line-height: 19px; color: var(--muted);
  }

  /* Collections */
  .section-title {
    font-family: "PT Sans Narrow", sans-serif; font-weight: 700; font-size: 14px;
    letter-spacing: .2px;
  }
  .collection-photo { top: 664px; width: 236px; height: 123px; background: #fff; border: 1px solid #ccc; }
  .collection-photo .shade { position: absolute; inset: 12px 60px; border-radius: 50%; }
  .carousel-arrows { left: 878px; top: 627px; }

  /* Lower row */
  .blog-thumb {
    left: 122px; top: 839px; width: 80px; height: 66px;
    background: radial-gradient(circle at 50% 45%, #7a4fb0 0%, #d9d9de 45%, #ffffff 80%);
    border: 2px solid #e5e5e5;
  }
  .blog-meta { font-family: Arial, sans-serif; font-size: 10px; font-weight: 700; }
  .blog-text { left: 122px; top: 916px; width: 220px; font-size: 10px; line-height: 17.5px; }

  .custom-card {
    left: 362px; top: 838px; width: 196px; height: 89px; background: #fff;
    border: 1px solid #ccc;
  }
  .custom-card .pendant {
    position: absolute; left: 10px; top: 10px; width: 62px; height: 66px;
    background: radial-gradient(circle, #e0e0e2 0%, #8d8d90 55%, #ffffff 85%);
  }
  .custom-card .card-title {
    position: absolute; left: 84px; top: 10px; width: 100px; text-align: center;
    font-family: "PT Sans Narrow", sans-serif; font-weight: 700; font-size: 13px; line-height: 15px; color: #2a2a2c;
  }
  .custom-card .card-text {
    position: absolute; left: 71px; top: 53px; width: 122px;
    font-size: 9px; line-height: 11px; color: #2a2a2c;
  }
  .click-button {
    left: 362px; top: 942px; width: 121px; height: 30px;
    background: linear-gradient(#5c5c5e, #232325); border-radius: 3px;
    font-family: "PT Sans Narrow", sans-serif; font-weight: 700; font-size: 14px;
    padding: 4px 0 0 19px;
  }

  .quick-links { left: 611px; top: 843px; font-size: 11px; color: var(--muted); }
  .quick-links li { list-style: none; height: 27px; }

  .quote-form { left: 725px; top: 834px; width: 174px; }
  .quote-form .field {
    height: 20px; border: 1px solid var(--field-border); margin-bottom: 3px;
    background: #111113; font-size: 8.5px; font-weight: 700; padding: 4px 0 0 7px;
  }
  .quote-form .submit {
    margin: 6px 0 0 107px; width: 67px; height: 19px; background: #d8d8da;
    color: #222; font-size: 13px; font-weight: 700; text-align: center; line-height: 19px;
  }

  .taglines {
    left: 0; width: 1016px; top: 998px; padding-left: 44px; text-align: center;
    font-size: 16px; font-weight: 700; color: var(--tagline); line-height: 33.5px;
  }

  /* Footer */
  .site-footer {
    left: 0; top: 1112px; width: 1016px; height: 88px;
    background: var(--footer-bg); border-top: 3px solid var(--footer-rule);
  }
  .footer-links { left: 123px; top: 23px; font-size: 11px; font-weight: 700; }
  .copyright { left: 122px; top: 51px; font-family: Arial, sans-serif; font-size: 10px; }
  .social { left: 794px; top: 33px; display: flex; gap: 5px; }
  .social span { width: 23px; height: 23px; border-radius: 50%; border: 2px solid #d8d8da; background: #3d5c9c; }
  .social span:nth-child(2) { background: #2aa9e0; }
  .social span:nth-child(3) { background: #1b7ab8; }
  .social span:nth-child(4) { background: #f08c1a; }
</style>
</head>
<body>

<header>
  <div class="abs brand">
    <span class="brand-mark"></span>
    <span class="brand-name">Velmora Gems</span>
  </div>

  <nav class="abs account-links">
    <a href="#">Register</a><span class="sep">/</span>
    <a href="#">Log In</a><span class="sep">/</span>
    <a href="#">Wish List</a><span class="sep">/</span>
    <a href="#" class="cart">My Cart &nbsp;0 itmes</a>
  </nav>

  <div class="abs search">
    <span>Search</span>
    <svg width="12" height="12" viewBox="0 0 12 12" aria-hidden="true">
      <circle cx="4.5" cy="4.5" r="3.3" fill="none" stroke="#111" stroke-width="1.8"/>
      <line x1="7" y1="7" x2="11" y2="11" stroke="#111" stroke-width="2.4" stroke-linecap="round"/>
    </svg>
  </div>

  <nav class="abs main-nav">
    <a href="#">COLLECTION GALLERY</a>
    <a href="#">ABOUT US</a>
    <a href="#">BLOG</a>
    <a href="#">EDUCATION</a>
    <a href="#">BUYING FROM US</a>
    <a href="#">TESTIMONIALS</a>
    <a href="#">48 HOUR PRODUCT OFFER</a>
  </nav>
</header>

<section class="abs hero">
  <div class="hero-panel">
    <div class="hero-photo" role="img" aria-label="Platinum diamond engagement rings with emerald-cut and princess-cut stones"></div>
    <h1 class="hero-title">WE DO CUSTOM MADE</h1>
    <p class="hero-sub">NECKLACES, EARRINGS, BRACELETS ETC</p>
    <a href="#" class="hero-button">CUSTOM JEWELLERY</a>
    <p class="hero-note">Create your own jewellery</p>
    <div class="hero-dots"><span></span><span class="active"></span><span></span></div>
  </div>
</section>

<h2 class="abs welcome-title">WELCOME TO OUR COMPANY</h2>
<p class="abs welcome-text">The standard chunk of Lorem Ipsum used since the 1500s is reproduced below for those interested. Sections 1.10.32 and &nbsp;"de Finibus Bonorum et Malorum" by Cicero are also reproduced in their exact original form, accompanied by English versions from the 1914 translation by H. Rackham.The standard chunk of Lorem for those in their exact original form, The standard chunk of Ipsum used since the 1500s is reproduced below for those interested. Sections Sections 1.10.32 and 1.10.33 from "de Finibus Bonorum et Malorum" by Cicero reproduced below for those interested. Sections &nbsp;"de Finibus Bonorum et Malorum" by Cicero.</p>

<h3 class="abs section-title" style="left:121px;top:624px;">NECKLACES COLLECTIONS</h3>
<h3 class="abs section-title" style="left:390px;top:624px;">EARRINGS COLLECTIONS</h3>
<h3 class="abs section-title" style="left:665px;top:624px;">BRACELETS COLLECTIONS</h3>
<svg class="abs carousel-arrows" width="24" height="14" viewBox="0 0 24 14" aria-hidden="true">
  <polygon points="8,0 8,14 1,7" fill="#8a8a8c"/>
  <polygon points="16,0 16,14 23,7" fill="#cfcfd1"/>
</svg>

<div class="abs collection-photo" style="left:121px;">
  <div class="shade" role="img" aria-label="Silver swirl pendant set with diamonds" style="background:radial-gradient(circle,#bdbdc1 0%,#ffffff 70%);"></div>
</div>
<div class="abs collection-photo" style="left:392px;">
  <div class="shade" role="img" aria-label="Gold drop earrings with green pear-shaped stones" style="background:radial-gradient(circle,#a9d4b4 0%,#d8b978 40%,#ffffff 75%);"></div>
</div>
<div class="abs collection-photo" style="left:664px;">
  <div class="shade" role="img" aria-label="Silver scroll bracelet with diamond accents" style="background:radial-gradient(circle,#c4c4c8 0%,#ffffff 70%);"></div>
</div>

<h3 class="abs section-title" style="left:121px;top:810px;">BLOG</h3>
<div class="abs blog-thumb" role="img" aria-label="Ring with purple centre stone"></div>
<p class="abs blog-meta" style="left:209px;top:856px;">MARVESSI SALE</p>
<p class="abs blog-meta" style="left:209px;top:878px;">JUNE 21ST</p>
<p class="abs blog-text">which don't loin the middle of text. All the Lorem Ipsum generators on the Internet tend to repeat predefined chunks as necessary</p>

<h3 class="abs section-title" style="left:362px;top:809px;">CUSTOM JEWELLERY</h3>
<div class="abs custom-card">
  <div class="pendant" role="img" aria-label="Diamond pendant"></div>
  <p class="card-title">Create your<br>own jewellery</p>
  <p class="card-text">All the Lorem Ipsum tors on the Internet tend ty</p>
</div>
<a href="#" class="abs click-button">Click Here</a>

<h3 class="abs section-title" style="left:610px;top:810px;">ENGAGEMENT RING</h3>
<ul class="abs quick-links">
  <li>Collection Gallery</li>
  <li>About Us</li>
  <li>Blog</li>
  <li>Education</li>
  <li>Buying From Us</li>
</ul>
<form class="abs quote-form">
  <div class="field">Name :</div>
  <div class="field">Phone :</div>
  <div class="field">Email :</div>
  <div class="field">Competitor Link &nbsp;:</div>
  <div class="field">Budget &nbsp;:</div>
  <div class="submit">Submit</div>
</form>

<div class="abs taglines">
  <p>Exquisite craftsmanship Finest quality diamonds</p>
  <p>Will beat any competitors price by twenty to seventy percent guaranteed</p>
  <p>Price quotes within 24 hours</p>
</div>

<footer class="abs site-footer">
  <p class="abs footer-links">Cutomer Care | Faq | Cantact Us | Term &amp; Conditions | Sitemap</p>
  <p class="abs copyright">Copyrights @ 2013 All Rights Reserved</p>
  <div class="abs social" aria-label="Social links"><span></span><span></span><span></span><span></span></div>
</footer>

</body>
</html>
```